Fine Art business needs new website

We need a simple website with a home page, about us page, New sculptures, Sold sculptures, and a contact us page.Our sculptures are very high end one of a kind pieces. As such we need the site to be VERY elegant and professional. Lastly, because I'll be updating pictures on the website on a monthly basis it needs to be user friendly to update (Wordpress is preferred). The only branding we have so far for the business is a business card.
Updates
I wasn't completely ready when this project launched, also I am on the road right now and haven't been able to be as responsive to all you designers as I would like. I will work on giving feedback to all the top designs we've received so far. Thank you all so much for your participation and hardwork.
Target Market(s)
High end customers (affluent), art collectors, interior decorators/designers
Industry/Entity Type
Art Gallery
Coding
Coded - Design and coding required
Number of Pages Required
5+ page
Requirements
Must have
- Easily editable picture gallery for myself so that I can add new pieces(pictures of the pieces), remove sold pieces, etc. I would like the website to be built in wordpress so I can update it. I currently use sitekeeperpro through Netbirch for my other business website and would like to do the same for this one.
- Pages:
- -Intro page with featured pieces
- -Current pieces gallery (for sale) mainly a picture gallery
- -Sculptures archive (sold pieces) another picture gallery
- -About us: Pull-down of -about the artist (attached content)
- -Artistic Process (attached content)
- -Show Schedule:
- -one page dedicated to "friends of QMW" (basically a link page)
- TO BE CLEAR "www.lanternhollow.com" IS A TOTALLY DIFFERENT SITE AND I'M NOT TRYING TO COMBINE THE TWO OR JOIN THEM INTO ONE. This page needs be more elegant and seperate from the Lantern Hollow site.
- UPDATE: I'd like a link to the QMW Facebook page: https://www.facebook.com/quillmarkworks/
Nice to have
- I would like the pictures on the gallery pages able to have text connected with them (Materials, price)
- I would like the site style and fonts to be similar to our business cards we've already had designed (picture attached).
Should not have
- Too much flash or other things that will make the site slow to load.

```html
<!DOCTYPE html>
<html lang="en">
<head>
<meta charset="utf-8">
<title>Quill Mark Works — Home and About Us</title>
<link href="https://fonts.googleapis.com/css2?family=Lato:wght@400;700&family=Playfair+Display:wght@400&display=swap" rel="stylesheet">
<style>
  :root{
    --stage:#7a7a7a;
    --paper:#ffffff;
    --mist:#f3f3f3;
    --navbar:#eeeeee;
    --ink:#111111;
    --night:#000000;
    --accent:#1a1adc;
    --amethyst-dark:#2b1846;
    --amethyst:#6a4a9a;
    --amethyst-light:#b7a3d6;
    --agate-blue:#7d8fae;
    --agate-pale:#e6e3dc;
    --photo-warm:#8a7358;
    --photo-cool:#5b7aa6;
  }
  *{box-sizing:border-box;margin:0;padding:0}
  html,body{width:1200px;height:1200px;overflow:hidden;background:var(--stage)}
  body{position:relative;font-family:'Lato',sans-serif;color:var(--ink)}
  .page{position:absolute;top:0;height:1200px;background:var(--paper);overflow:hidden}
  .page--home{left:46px;width:473px}
  .page--about{left:577px;width:564px}
  .abs{position:absolute}
  .serif{font-family:'Playfair Display',serif;font-weight:400}

  .navbar{position:absolute;left:0;top:0;width:100%;background:var(--navbar)}
  .navbar__logo{position:absolute;color:var(--accent);text-transform:uppercase}
  .navbar__item{position:absolute;text-transform:uppercase;color:var(--ink)}
  .navbar__item--active{color:var(--accent)}
  .navbar__sep{position:absolute;width:1px;background:#333}

  .page--home .navbar{height:32px}
  .page--home .navbar__logo,.page--home .navbar__item{font-size:5px;top:14px}
  .page--home .navbar__sep{top:12px;height:9px}
  .page--about .navbar{height:38px}
  .page--about .navbar__logo,.page--about .navbar__item{font-size:6.5px;top:17px}
  .page--about .navbar__sep{top:15px;height:11px}

  .hero-title{position:absolute;left:0;width:100%;top:214px;text-align:center;font-size:18px;letter-spacing:3px;color:#555}
  .about-band{position:absolute;left:0;top:267px;width:100%;height:189px;background:var(--night);color:#fff}
  .about-band__title{position:absolute;left:0;width:100%;top:20px;text-align:center;font-size:13px}
  .photo{position:absolute}
  .small-copy{position:absolute;font-size:4.4px;line-height:6.2px}
  .about-band .small-copy{color:#fff;left:230px;top:52px;width:165px}
  .read-more{position:absolute;left:230px;top:107px;font-size:5px;color:var(--accent)}

  .gallery{position:absolute;left:0;top:456px;width:100%;height:602px;background:var(--mist)}
  .piece__name{position:absolute;font-size:12px;letter-spacing:.3px}
  .piece .small-copy{width:165px;color:#222}
  .buy{position:absolute;width:34px;height:16px;border:1.2px solid var(--accent);border-radius:9px;color:var(--accent);font-size:5.5px;text-align:center;line-height:14px}

  .footer{position:absolute;left:0;width:100%;bottom:0;background:var(--night);color:#fff;overflow:hidden}
  .footer__heading{position:absolute;color:var(--accent);text-transform:uppercase}
  .footer__link{position:absolute}
  .footer__title{position:absolute;left:0;width:100%;text-align:center;letter-spacing:1px}
  .footer__minor{position:absolute;color:var(--accent)}
  .footer__icons{position:absolute;display:flex}
  .footer__icons span{display:block;border-radius:50%;background:#cfcfcf}
  .footer__contact{position:absolute}

  .page--home .footer{height:142px}
  .page--home .footer__heading,.page--home .footer__minor{font-size:4.5px}
  .page--home .footer__link,.page--home .footer__contact{font-size:4.5px}
  .page--home .footer__title{top:34px;font-size:14px}
  .page--home .footer__icons{gap:7px}
  .page--home .footer__icons span{width:5px;height:5px}

  .page--about .footer{height:167px}
  .page--about .footer__heading,.page--about .footer__minor{font-size:5.5px}
  .page--about .footer__link,.page--about .footer__contact{font-size:5.5px}
  .page--about .footer__title{top:32px;font-size:17px}
  .page--about .footer__icons{gap:9px}
  .page--about .footer__icons span{width:6px;height:6px}

  .meet-title{position:absolute;left:0;width:100%;top:66px;text-align:center;font-size:21px;letter-spacing:.5px}
  .rule{position:absolute;height:1.5px;background:var(--accent)}
  .story-band{position:absolute;left:0;top:210px;width:100%;height:390px;background:var(--mist)}
  .story{position:absolute;font-size:8px;line-height:13.2px;color:#222}
  .artist__name{position:absolute;font-size:15.5px;letter-spacing:.3px}
  .artist__bio{position:absolute;font-size:6.5px}
</style>
</head>
<body>

<!-- Home page -->
<section class="page page--home">
  <header class="navbar">
    <span class="navbar__logo" style="left:50px;top:18px">Logo</span>
    <span class="navbar__item navbar__item--active" style="left:187px">Home</span>
    <span class="navbar__sep" style="left:219px"></span>
    <span class="navbar__item" style="left:236px">About us</span>
    <span class="navbar__sep" style="left:275px"></span>
    <span class="navbar__item" style="left:288px">Gallery</span>
    <span class="navbar__sep" style="left:325px"></span>
    <span class="navbar__item" style="left:339px">Artistic process</span>
    <span class="navbar__sep" style="left:396px"></span>
    <span class="navbar__item" style="left:408px">Contact us</span>
  </header>

  <svg class="abs" style="left:0;top:32px" width="473" height="235" role="img" aria-label="Photograph of an arched amethyst geode cluster">
    <defs>
      <linearGradient id="amethystArch" x1="0" y1="0" x2="0" y2="1">
        <stop offset="0" stop-color="var(--amethyst-light)"/>
        <stop offset=".45" stop-color="var(--amethyst)"/>
        <stop offset="1" stop-color="var(--amethyst-dark)"/>
      </linearGradient>
    </defs>
    <path d="M15 130 C40 80 110 50 180 22 C230 5 270 20 300 60 C330 95 380 95 430 95 L473 100 L473 235 L440 225 C420 205 405 170 395 140 C360 110 330 140 300 130 C260 95 220 80 180 95 C130 115 90 130 70 170 C50 160 30 160 15 130 Z" fill="url(#amethystArch)"/>
  </svg>
  <h1 class="hero-title serif">QUILL MARK WORKS</h1>

  <section class="about-band">
    <h2 class="about-band__title serif">ABOUT US</h2>
    <div class="photo" style="left:42px;top:53px;width:151px;height:112px;background:linear-gradient(90deg,var(--photo-warm),#a9a9a9 50%,var(--photo-cool))" role="img" aria-label="Photo of the two artists in respirator masks in the workshop"></div>
    <p class="small-copy">We are a small family studio shaping agate, geode and fossil stone into one of a kind sculpture. Each piece is cut, ground and polished by hand over many weeks, so that the natural pattern of the stone leads the form and every finished work stands alone in its own character and light.</p>
    <span class="read-more">READ MORE</span>
  </section>

  <section class="gallery">
    <article class="piece">
      <div class="photo" style="left:94px;top:22px;width:84px;height:252px;border-radius:40px 40px 30px 30px;background:linear-gradient(180deg,var(--agate-blue),var(--agate-pale) 45%,var(--agate-blue) 75%,var(--photo-warm))" role="img" aria-label="Photo of a tall banded agate sculpture on a stone base"></div>
      <h3 class="piece__name serif" style="left:251px;top:50px">SCULPTURE NAME</h3>
      <p class="small-copy" style="left:251px;top:81px">A tall slab of banded agate rises from a polished jasper base. Blue and white bands wrap a crystal core, and the edge is left natural so the outer rind frames the stone. Height about thirty inches, signed and dated by the artist on the base.</p>
      <span class="buy" style="left:251px;top:148px">BUY</span>
    </article>
    <article class="piece">
      <h3 class="piece__name serif" style="left:58px;top:324px">SCULPTURE NAME</h3>
      <p class="small-copy" style="left:58px;top:355px">A tall slab of banded agate rises from a polished jasper base. Blue and white bands wrap a crystal core, and the edge is left natural so the outer rind frames the stone. Height about thirty inches, signed and dated by the artist on the base.</p>
      <span class="buy" style="left:59px;top:427px">BUY</span>
      <div class="photo" style="left:284px;top:316px;width:86px;height:252px;border-radius:40px 40px 30px 30px;background:linear-gradient(180deg,var(--agate-blue),var(--agate-pale) 45%,var(--agate-blue) 75%,var(--photo-warm))" role="img" aria-label="Photo of a tall banded agate sculpture on a stone base"></div>
    </article>
  </section>

  <footer class="footer">
    <div class="abs" style="left:60px;top:62px;width:380px;height:90px;border-radius:50% 50% 0 0;background:radial-gradient(ellipse at 50% 30%,var(--amethyst-light),var(--amethyst) 45%,var(--amethyst-dark) 80%,transparent)" role="img" aria-label="Decorative amethyst crystal photo"></div>
    <span class="footer__heading" style="left:34px;top:28px">Quick links</span>
    <span class="footer__link" style="left:34px;top:43px">Home</span>
    <span class="footer__link" style="left:34px;top:57px">About us</span>
    <span class="footer__link" style="left:34px;top:71px">Gallery</span>
    <span class="footer__link" style="left:34px;top:85px">Artistic process</span>
    <span class="footer__link" style="left:34px;top:99px">Contact</span>
    <h2 class="footer__title serif">QUILL MARK WORKS</h2>
    <span class="footer__minor" style="left:370px;top:28px">Stay connected</span>
    <div class="footer__icons" style="left:370px;top:42px"><span></span><span></span><span></span><span></span></div>
    <span class="footer__minor" style="left:370px;top:66px">Contact us</span>
    <span class="footer__contact" style="left:370px;top:78px">e-mail: corey@lanternhollow.com</span>
    <span class="footer__contact" style="left:370px;top:92px">phone: (555) 310-4826</span>
  </footer>
</section>

<!-- About us page -->
<section class="page page--about">
  <header class="navbar">
    <span class="navbar__logo" style="left:59px;top:21px">Logo</span>
    <span class="navbar__item" style="left:221px">Home</span>
    <span class="navbar__sep" style="left:259px"></span>
    <span class="navbar__item navbar__item--active" style="left:278px">About us</span>
    <span class="navbar__sep" style="left:324px"></span>
    <span class="navbar__item" style="left:341px">Gallery</span>
    <span class="navbar__sep" style="left:385px"></span>
    <span class="navbar__item" style="left:402px">Artistic process</span>
    <span class="navbar__sep" style="left:470px"></span>
    <span class="navbar__item" style="left:485px">Contact us</span>
  </header>

  <h1 class="meet-title serif">MEET THE ARTISTS</h1>
  <span class="rule" style="left:243px;top:104px;width:73px"></span>

  <section class="story-band">
    <span class="rule" style="left:45px;top:122px;width:70px"></span>
    <p class="story" style="left:47px;top:142px;width:225px">Hal Brennick has been mastering the Lapidary Arts since the late 1980’s. Somewhere in the middle of this new career of his he recruited his kids into the shop to help him with the ever increasing demand for his one of a kind fossil and mineral sculptures. An unintended (or possibly intended) consequence of bringing his children into the fold is they eventually fell in love with rocks and became proficient in many of the lapidary techniques.</p>
    <p class="story" style="left:301px;top:205px;width:222px">Fast forward to 2012, after graduating college and working several years in the real world two of Hal’s children, Corwin and Tamsin, decided to work with their Father full-time as a chance to be closer to family while at the same time seeing different parts of the US. Through the past 6 years all of Hal’s children have continued to contribute to the family livelihood on a part-time basis with the exception of Corey who is now a full time Artist alongside his Father. Both Hal and Corey have their own unique styles, yet on occasion they will combine their talents to create a collaborative masterpiece.</p>
  </section>
  <div class="photo" style="left:177px;top:132px;width:221px;height:166px;background:linear-gradient(90deg,var(--photo-warm),#a9a9a9 50%,var(--photo-cool))" role="img" aria-label="Photo of the two artists in respirator masks in the workshop"></div>

  <article class="artist">
    <div class="photo" style="left:45px;top:623px;width:225px;height:169px;background:linear-gradient(180deg,#8c8f88,#5a4a3a 60%,#3d3a2a)" role="img" aria-label="Portrait photo of Harold Brennick in a brown hat outdoors"></div>
    <span class="rule" style="left:249px;top:667px;width:68px"></span>
    <h2 class="artist__name serif" style="left:299px;top:681px">HAROLD “HAL” BRENNICK</h2>
    <span class="artist__bio" style="left:299px;top:713px">BIO</span>
  </article>

  <article class="artist">
    <span class="rule" style="left:247px;top:872px;width:70px"></span>
    <h2 class="artist__name serif" style="right:298px;top:886px;text-align:right">COREY BRENNICK</h2>
    <span class="artist__bio" style="right:298px;top:919px">BIO</span>
    <div class="photo" style="left:295px;top:835px;width:229px;height:152px;background:linear-gradient(180deg,#c9c3bb,#8c7a68 55%,#e8ecf0)" role="img" aria-label="Portrait photo of Corey Brennick outdoors in winter"></div>
  </article>

  <footer class="footer">
    <div class="abs" style="left:150px;top:72px;width:370px;height:110px;border-radius:50% 50% 0 0;background:radial-gradient(ellipse at 50% 30%,var(--amethyst-light),var(--amethyst) 45%,var(--amethyst-dark) 80%,transparent)" role="img" aria-label="Decorative amethyst crystal photo"></div>
    <span class="footer__heading" style="left:40px;top:32px">Quick links</span>
    <span class="footer__link" style="left:40px;top:50px">Home</span>
    <span class="footer__link" style="left:40px;top:67px">About us</span>
    <span class="footer__link" style="left:40px;top:84px">Gallery</span>
    <span class="footer__link" style="left:40px;top:101px">Artistic process</span>
    <span class="footer__link" style="left:40px;top:118px">Contact</span>
    <h2 class="footer__title serif">QUILL MARK WORKS</h2>
    <span class="footer__minor" style="left:441px;top:32px">Stay connected</span>
    <div class="footer__icons" style="left:441px;top:49px"><span></span><span></span><span></span><span></span></div>
    <span class="footer__minor" style="left:441px;top:77px">Contact us</span>
    <span class="footer__contact" style="left:441px;top:91px">e-mail: corey@lanternhollow.com</span>
    <span class="footer__contact" style="left:441px;top:108px">phone: (555) 310-4826</span>
    <span class="buy" style="left:70px;top:137px;width:40px;height:18px;line-height:16px">BUY</span>
  </footer>
</section>

</body>
</html>
```